Multilingual Website for a Curaline Company

We need a multilingual Website for our Curaline company that sells gloves and masks, the website should have 3-5 subpages on 5 different languages.

Industry/Entity Type

Medtech

Number of Pages Required

5+ page

Requirements
Must have
• Unique Design - No template
Should not have
• No Templates

```html
<!DOCTYPE html>
<html lang="en">
<head>
<meta charset="utf-8">
<title>Curaline — Healthcare Protective Supplies</title>
<link rel="stylesheet" href="https://fonts.googleapis.com/css2?family=Lato:ital,wght@0,300;0,400;0,700;1,400&display=swap">
<style>
:root{
  --green-dark:#1b2a0e;
  --green-mid:#4a6b2a;
  --green-logo:#6a9a2e;
  --beige:#f3f0e9;
  --card-body:#f4f1ea;
  --white:#ffffff;
  --text:#3a3a3a;
  --muted:#8a8a8a;
}
*{margin:0;padding:0;box-sizing:border-box}
html,body{width:1200px;height:3034px;overflow:hidden}
body{font-family:'Lato',sans-serif;background:var(--white);position:relative;color:var(--text)}
.abs{position:absolute}

/* header */
.site-header{left:0;top:0;width:1200px;height:67px;background:var(--green-dark)}
.brand{font-weight:700;font-size:34px;color:var(--green-logo);display:flex;align-items:center;gap:8px;letter-spacing:-.5px}
.brand-dot{width:14px;height:14px;border-radius:50%;background:var(--green-logo)}
.site-header .brand{left:150px;top:14px}
.main-nav{left:458px;top:22px;display:flex;gap:32px}
.main-nav a{color:var(--white);font-weight:700;font-size:17px;text-decoration:none}
.header-tools{left:878px;top:22px;display:flex;gap:22px;align-items:center}
.cart-count{left:1036px;top:19px;width:14px;height:14px;border-radius:50%;background:var(--green-logo);color:#fff;font-size:9px;text-align:center;line-height:14px}

/* hero */
.hero{left:0;top:67px;width:1200px;height:522px;background:linear-gradient(90deg,#2f4a1f 0%,#4b6a33 35%,#a07a62 62%,#c9a58e 78%,#d6d3cf 100%)}
.hero-kicker{left:150px;top:244px;color:#fff;font-size:23px;font-weight:400}
.hero-title{left:150px;top:274px;color:#fff;font-size:36px;font-weight:700;line-height:45px}
.btn-light{left:150px;top:373px;width:150px;height:44px;background:var(--beige);border-radius:3px;font-size:12px;font-weight:700;color:#222;display:flex;align-items:center;justify-content:center}

/* feature band */
.feature-band{left:0;top:589px;width:1200px;height:112px}
.feature{top:589px;height:112px;color:#fff;font-size:28px;font-weight:700;display:flex;align-items:center;justify-content:center}

.beige{background:var(--beige)}

/* categories */
.category{top:738px;width:600px;height:375px;color:#fff;font-size:28px;font-weight:700;text-align:center;display:flex;align-items:center;justify-content:center;line-height:40px}

/* tabs */
.tabs{left:0;top:1156px;width:1200px;height:66px;background:var(--green-dark)}
.tab{top:1156px;height:66px;width:300px;color:#fff;font-size:27px;display:flex;align-items:center;justify-content:center}
.tab.active{background:var(--green-mid)}

/* products */
.product{width:293px;height:400px;background:var(--card-body);box-shadow:0 1px 6px rgba(0,0,0,.12)}
.product-photo{position:absolute;left:0;top:0;width:293px;height:188px;background:#fff}
.product-photo span{position:absolute;left:60px;top:35px;width:173px;height:118px;border-radius:6px}
.product-name{position:absolute;left:15px;top:206px;font-size:22px;color:#333}
.product-price{position:absolute;right:15px;top:208px;font-size:19px;color:#333}
.product-desc{position:absolute;left:16px;top:238px;width:262px;font-size:13.5px;line-height:20px;color:var(--muted);font-weight:300}
.btn-cart{position:absolute;left:72px;top:338px;width:150px;height:45px;background:var(--green-mid);color:#fff;font-size:12px;font-weight:700;display:flex;align-items:center;justify-content:center;border-radius:2px}

/* about / contact */
.section-title{font-size:28px;font-weight:700;color:var(--green-dark)}
.section-title::after{content:"";display:block;width:75px;height:4px;background:var(--green-mid);margin-top:3px}
.about-text{width:455px;font-size:14px;line-height:20.5px;color:#333}
.field{left:150px;width:435px;border:2px solid var(--green-mid);background:#fff;font-size:13px;font-style:italic;color:#888;padding:0 13px;display:flex;align-items:center}
.field.message{align-items:flex-start;padding-top:14px}
.btn-submit{left:435px;top:2691px;width:150px;height:45px;background:var(--green-mid);color:#fff;font-size:12px;font-weight:700;display:flex;align-items:center;justify-content:center}
.map{left:705px;top:2418px;width:345px;height:317px;background:linear-gradient(135deg,#a9d3f5 0%,#b8dcf6 45%,#c6dfb4 60%,#a9d3f5 100%)}

/* footer */
.site-footer{left:0;top:2773px;width:1200px;height:224px;background:var(--green-dark)}
.footer-about{left:153px;top:2843px;width:260px;color:#fff;font-size:13px;line-height:20.5px}
.footer-heading{color:#fff;font-size:17px;font-weight:700}
.footer-link{color:#fff;font-size:13.5px}
.footer-contact{left:919px;color:#fff;font-size:13.5px;line-height:20px}
.bottom-bar{left:0;top:2997px;width:1200px;height:37px;background:var(--green-mid);color:#fff;font-size:13px;display:flex;align-items:center;justify-content:center}
</style>
</head>
<body>

<header class="site-header abs"></header>
<div class="brand abs"><span class="brand-dot"></span>Curaline</div>
<nav class="main-nav abs"><a>Home</a><a>Shop</a><a>About</a><a>Contact</a></nav>
<div class="header-tools abs">
  <svg width="24" height="16" viewBox="0 0 24 16" aria-label="English"><rect width="24" height="16" fill="#2b3f8f"/><path d="M0 0L24 16M24 0L0 16" stroke="#fff" stroke-width="3"/><path d="M12 0V16M0 8H24" stroke="#fff" stroke-width="5"/><path d="M12 0V16M0 8H24" stroke="#c8102e" stroke-width="2.5"/></svg>
  <svg width="26" height="26" viewBox="0 0 26 26"><circle cx="11" cy="11" r="8" fill="none" stroke="#fff" stroke-width="2"/><path d="M17 17L24 24" stroke="#fff" stroke-width="2"/></svg>
  <svg width="26" height="28" viewBox="0 0 26 28"><circle cx="13" cy="9" r="6" fill="none" stroke="#fff" stroke-width="2"/><path d="M2 27C3 19 8 16 13 16S23 19 24 27" fill="none" stroke="#fff" stroke-width="2"/></svg>
  <svg width="28" height="26" viewBox="0 0 28 26"><path d="M1 2H5L8 17H23L26 7H7" fill="none" stroke="#fff" stroke-width="2"/><circle cx="10" cy="22" r="2" fill="#fff"/><circle cx="21" cy="22" r="2" fill="#fff"/></svg>
</div>
<div class="cart-count abs">0</div>

<section class="hero abs" role="img" aria-label="Photo of a man wearing a protective respirator mask"></section>
<p class="hero-kicker abs">Your safety is our top priority.</p>
<h1 class="hero-title abs">Your trusted supplier for<br>healthcare protective supplies.</h1>
<div class="btn-light abs">Shop now</div>

<svg class="feature-band abs" viewBox="0 0 1200 112" width="1200" height="112">
  <rect width="1200" height="112" fill="#1b2a0e"/>
  <polygon points="394,0 871,0 801,112 327,112" fill="#4a6b2a"/>
</svg>
<div class="feature abs" style="left:0;width:398px">Free Shipping</div>
<div class="feature abs" style="left:400px;width:400px">Worldwide Shipping</div>
<div class="feature abs" style="left:835px;width:400px;margin-top:-3px">Free Samples</div>

<div class="beige abs" style="left:0;top:701px;width:1200px;height:37px"></div>
<div class="category abs" role="img" aria-label="Photo of stacked disposable face masks" style="left:0;background:linear-gradient(135deg,#4d5c6a,#5f6e7c 50%,#4a5866)">Disposable and reusable<br>face masks</div>
<div class="category abs" role="img" aria-label="Photo of hands in disposable medical gloves" style="left:600px;background:linear-gradient(135deg,#5a6870,#66747b 60%,#56646c)">Disposable medical gloves<br>to protect your hands</div>
<div class="beige abs" style="left:0;top:1113px;width:1200px;height:43px"></div>

<div class="tabs abs"></div>
<div class="tab active abs" style="left:150px">Masks</div>
<div class="tab abs" style="left:449px">Gloves</div>
<div class="tab abs" style="left:749px">Others</div>

<article class="product abs" style="left:150px;top:1261px"><div class="product-photo"><span role="img" aria-label="Product photo of a 3 ply face mask box" style="background:linear-gradient(135deg,#dfe8f3,#2a4b8c)"></span></div><h3 class="product-name">Disposable Mask</h3><span class="product-price">$16.00</span><p class="product-desc">Lorem ipsum dolor sit amet, consectetur elit. Morbi pellentesque, nisi ac tincidunt varius, erat nulla tempor est, ac malesuada ex quam sit amet ipsum.</p><div class="btn-cart">Add to cart</div></article>
<article class="product abs" style="left:453px;top:1261px"><div class="product-photo"><span role="img" aria-label="Product photo of a surgical mask box" style="background:linear-gradient(135deg,#cfe6f5,#4aa3dc)"></span></div><h3 class="product-name">Surgical Mask</h3><span class="product-price">$22.00</span><p class="product-desc">Lorem ipsum dolor sit amet, consectetur elit. Morbi pellentesque, nisi ac tincidunt varius, erat nulla tempor est, ac malesuada ex quam sit amet ipsum.</p><div class="btn-cart">Add to cart</div></article>
<article class="product abs" style="left:757px;top:1261px"><div class="product-photo"><span role="img" aria-label="Product photo of a reusable black mask and box" style="background:linear-gradient(135deg,#eef0f2,#222)"></span></div><h3 class="product-name">Reusable Mask</h3><span class="product-price">$26.00</span><p class="product-desc">Lorem ipsum dolor sit amet, consectetur elit. Morbi pellentesque, nisi ac tincidunt varius, erat nulla tempor est, ac malesuada ex quam sit amet ipsum.</p><div class="btn-cart">Add to cart</div></article>

<article class="product abs" style="left:150px;top:1673px"><div class="product-photo"><span role="img" aria-label="Product photo of an N95 mask with box" style="background:linear-gradient(135deg,#2e4a6c,#f2f2f2)"></span></div><h3 class="product-name">N95 Mask</h3><span class="product-price">$28.00</span><p class="product-desc">Lorem ipsum dolor sit amet, consectetur elit. Morbi pellentesque, nisi ac tincidunt varius, erat nulla tempor est, ac malesuada ex quam sit amet ipsum.</p><div class="btn-cart">Add to cart</div></article>
<article class="product abs" style="left:453px;top:1673px"><div class="product-photo"><span role="img" aria-label="Product photo of an N95 mask box" style="background:linear-gradient(135deg,#3aa6b5,#7fcad3)"></span></div><h3 class="product-name">N95 Mask</h3><span class="product-price">$38.00</span><p class="product-desc">Lorem ipsum dolor sit amet, consectetur elit. Morbi pellentesque, nisi ac tincidunt varius, erat nulla tempor est, ac malesuada ex quam sit amet ipsum.</p><div class="btn-cart">Add to cart</div></article>
<article class="product abs" style="left:757px;top:1673px"><div class="product-photo"><span role="img" aria-label="Product photo of a disposable mask box" style="background:linear-gradient(135deg,#1d3357,#e9edf2)"></span></div><h3 class="product-name">Disposable Mask</h3><span class="product-price">$18.00</span><p class="product-desc">Lorem ipsum dolor sit amet, consectetur elit. Morbi pellentesque, nisi ac tincidunt varius, erat nulla tempor est, ac malesuada ex quam sit amet ipsum.</p><div class="btn-cart">Add to cart</div></article>

<section class="beige abs" style="left:0;top:2111px;width:1200px;height:215px"></section>
<h2 class="section-title abs" style="left:150px;top:2141px">About us</h2>
<p class="about-text abs" style="left:150px;top:2188px">Lorem ipsum dolor sit amet, consectetur adipiscing elit. Quisque sem neque, vulputate nec varius sed, tincidunt non nisl. In consectetur at metus pellentesque efficitur. Nulla vulputate maximus justo, ac posuere purus semper dignissim. Donec viverra, ipsum vel pulvinar consectetur, lacus dui dictum risus, quis fermentum ligula leo ac nunc.</p>
<p class="about-text abs" style="left:617px;top:2188px">Lorem ipsum dolor sit amet, consectetur adipiscing elit. Quisque sem neque, vulputate nec varius sed, tincidunt non nisl. In consectetur at metus pellentesque efficitur. Nulla vulputate maximus justo, ac posuere purus semper dignissim.</p>

<h2 class="section-title abs" style="left:150px;top:2357px">Contact us</h2>
<div class="field abs" style="top:2418px;height:44px">Full Name</div>
<div class="field abs" style="top:2474px;height:44px">Email address</div>
<div class="field message abs" style="top:2531px;height:148px">Message</div>
<div class="btn-submit abs">Submit</div>
<div class="map abs" role="img" aria-label="Map showing the company location"></div>

<footer class="site-footer abs"></footer>
<div class="brand abs" style="left:150px;top:2790px"><span class="brand-dot"></span>Curaline</div>
<p class="footer-about abs">Lorem ipsum dolor sit amet, consectetur adipiscing elit. Morbi pellentesque, nisi ac tincidunt varius, erat nulla tempor est, ac malesuada ex quam sit amet ipsum.</p>
<h4 class="footer-heading abs" style="left:555px;top:2808px">Navigation</h4>
<span class="footer-link abs" style="left:555px;top:2841px">Home</span>
<span class="footer-link abs" style="left:555px;top:2868px">Shop</span>
<span class="footer-link abs" style="left:555px;top:2895px">About</span>
<span class="footer-link abs" style="left:555px;top:2922px">Contact</span>
<span class="footer-link abs" style="left:640px;top:2841px">Privacy Policy</span>
<span class="footer-link abs" style="left:640px;top:2868px">Returns &amp; Refunds</span>
<span class="footer-link abs" style="left:640px;top:2895px">FAQs</span>
<h4 class="footer-heading abs" style="left:885px;top:2808px">Contact Us</h4>
<svg class="abs" style="left:886px;top:2842px" width="16" height="22" viewBox="0 0 16 22"><path d="M8 21C8 21 1 12 1 8A7 7 0 0 1 15 8C15 12 8 21 8 21Z" fill="none" stroke="#fff" stroke-width="1.5"/><circle cx="8" cy="8" r="2.5" fill="none" stroke="#fff" stroke-width="1.5"/></svg>
<p class="footer-contact abs" style="top:2842px">Address, City, Country<br>Exact address</p>
<svg class="abs" style="left:886px;top:2901px" width="20" height="20" viewBox="0 0 20 20"><path d="M4 1L8 5L6 8C7 11 9 13 12 14L15 12L19 16L16 19C8 18 2 12 1 4Z" fill="#fff"/></svg>
<p class="footer-contact abs" style="top:2902px">+00 0 0000 00000</p>
<svg class="abs" style="left:886px;top:2945px" width="20" height="14" viewBox="0 0 20 14"><rect x="1" y="1" width="18" height="12" fill="none" stroke="#fff" stroke-width="1.5"/><path d="M1 1L10 8L19 1M1 13L8 7M19 13L12 7" fill="none" stroke="#fff" stroke-width="1.5"/></svg>
<p class="footer-contact abs" style="top:2942px">admin@curaline.example</p>
<div class="bottom-bar abs">Curaline 2020 All Rights Reserved.</div>

</body>
</html>
```